Garden Design Flier

I would like a PDF of this half page A4 flier in soft green tones with dark green leaves.

Target Market(s)

Home owners and real estate agents

Font styles to use
Serif
Other font styles liked:
• Papyrus

Colors
acd136
9bcb3c
cadf82
fefdec

Requirements
Must have
• Green tones
Nice to have
• Leaves, vines, lawns
Should not have
• Open to ideas, but classic style

```html
<!DOCTYPE html>
<html lang="en">
<head>
<meta charset="utf-8">
<title>Verdelle Gardens – Flier</title>
<link rel="stylesheet" href="https://fonts.googleapis.com/css2?family=Arimo:wght@700&family=Lobster+Two:ital,wght@1,400;1,700&display=swap">
<style>
  :root {
    --frame-green: #9bcb3c;
    --frame-lime: #acd136;
    --frame-soft: #cadf82;
    --paper: #fefdec;
    --paper-tint: #eef4cf;
    --leaf-dark: #3f6b1e;
    --brand-green: #6f9f2a;
    --vine-tint: rgba(202, 223, 130, 0.45);
    --ink: #1b2410;
  }
  * { box-sizing: border-box; margin: 0; padding: 0; }
  html, body { width: 1200px; height: 849px; overflow: hidden; background: #ffffff; }

  .flier {
    position: relative;
    width: 1200px;
    height: 849px;
    background: linear-gradient(135deg, var(--frame-lime), var(--frame-green));
    overflow: hidden;
    font-family: "Lobster Two", "Georgia", serif;
  }
  .flier__frame { position: absolute; inset: 0; }

  .flier__paper {
    position: absolute;
    left: 80px; top: 66px; right: 80px; bottom: 64px;
    background: radial-gradient(ellipse at center, var(--paper) 60%, var(--paper-tint) 100%);
  }

  .vines {
    position: absolute;
    background: linear-gradient(180deg, var(--vine-tint), rgba(202, 223, 130, 0.15));
    border-radius: 60px;
  }
  .vines--left  { left: 96px;  top: 90px; width: 250px; height: 670px; }
  .vines--right { right: 96px; top: 80px; width: 280px; height: 680px; }

  .brand {
    position: absolute;
    left: 0; right: 0; top: 0;
    height: 360px;
    color: var(--brand-green);
    font-family: "Lobster Two", "Georgia", serif;
    font-style: italic;
    font-weight: 700;
    text-align: center;
  }
  .brand__name {
    position: absolute; left: 0; right: 0; top: 96px;
    font-size: 128px; line-height: 1.3;
  }
  .brand__sub {
    position: absolute; left: 0; right: 0; top: 300px;
    font-size: 46px; line-height: 1; letter-spacing: 3px;
  }

  .credit {
    position: absolute;
    left: 0; right: 0; top: 368px;
    text-align: center;
    color: var(--ink);
    font-style: italic;
    font-weight: 700;
    font-size: 24px;
    line-height: 30px;
  }

  .steps {
    position: absolute;
    top: 472px; left: 0; right: 0; height: 58px;
    list-style: none;
  }
  .steps__item {
    position: absolute;
    top: 0; height: 58px;
    font-family: "Arimo", "Arial", sans-serif;
    font-weight: 700;
    font-size: 41px;
    letter-spacing: 1.5px;
    color: var(--leaf-dark);
    text-align: center;
    line-height: 58px;
  }

  .pitch {
    position: absolute;
    left: 0; right: 0; top: 561px;
    text-align: center;
    color: var(--ink);
    font-style: italic;
    font-weight: 700;
    font-size: 26px;
    line-height: 43px;
  }

  .contact {
    position: absolute;
    left: 0; right: 0; top: 693px;
    text-align: center;
    color: var(--ink);
    font-style: italic;
    font-weight: 700;
    font-size: 26px;
    word-spacing: 2px;
  }
  .contact__dot {
    display: inline-block;
    width: 13px; height: 13px;
    border-radius: 50%;
    background: var(--leaf-dark);
    margin: 0 12px;
    vertical-align: 3px;
  }
</style>
</head>
<body>
<main class="flier">
  <svg class="flier__frame" width="1200" height="849" viewBox="0 0 1200 849" aria-hidden="true">
    <rect x="14" y="14" width="1172" height="821" rx="24" fill="none" stroke="var(--frame-soft)" stroke-width="10" opacity="0.7"/>
  </svg>

  <div class="flier__paper"></div>
  <div class="vines vines--left" role="img" aria-label="Faint climbing vines with dark green leaves"></div>
  <div class="vines vines--right" role="img" aria-label="Faint climbing vines with dark green leaves"></div>

  <svg class="flier__frame" width="1200" height="849" viewBox="0 0 1200 849" aria-hidden="true">
    <rect x="72" y="56" width="1056" height="736" rx="20" fill="none" stroke="var(--paper)" stroke-width="7"/>
    <rect x="62" y="46" width="1076" height="756" rx="26" fill="none" stroke="var(--leaf-dark)" stroke-width="3" opacity="0.55"/>
  </svg>

  <h1 class="brand">
    <span class="brand__name">Verdelle</span>
    <span class="brand__sub">Gardens</span>
  </h1>

  <p class="credit">
    by Owen Hartley<br>
    Certificate 3. Horticulture. Coastline TC
  </p>

  <ul class="steps">
    <li class="steps__item" style="left:143px;width:172px;">Design</li>
    <li class="steps__item" style="left:341px;width:171px;">Install</li>
    <li class="steps__item" style="left:549px;width:149px;">Grow</li>
    <li class="steps__item" style="left:745px;width:149px;">Tend</li>
    <li class="steps__item" style="left:940px;width:149px;">Enjoy</li>
  </ul>
  <svg class="flier__frame" width="1200" height="849" viewBox="0 0 1200 849" aria-hidden="true">
    <g fill="none" stroke="var(--frame-green)" stroke-width="2" stroke-linecap="round">
      <path d="M147 477 H312 M147 528 H312"/>
      <path d="M344 477 H509 M344 528 H509"/>
      <path d="M552 477 H695 M552 528 H695"/>
      <path d="M748 477 H891 M748 528 H891"/>
      <path d="M943 477 H1086 M943 528 H1086"/>
      <path d="M143 475 v5 M315 475 v5 M143 525 v5 M315 525 v5"/>
      <path d="M341 475 v5 M512 475 v5 M341 525 v5 M512 525 v5"/>
      <path d="M549 475 v5 M698 475 v5 M549 525 v5 M698 525 v5"/>
      <path d="M745 475 v5 M894 475 v5 M745 525 v5 M894 525 v5"/>
      <path d="M940 475 v5 M1089 475 v5 M940 525 v5 M1089 525 v5"/>
    </g>
  </svg>

  <p class="pitch">
    All your gardening and landscaping needs from design and installation to general maintenance<br>
    Bespoke vegetable gardens and potager designs created to suit your site and requirements
  </p>

  <p class="contact">
    email: owen@verdellegardens.com.au<span class="contact__dot"></span>Mobile: 0400 - 318552<span class="contact__dot"></span>ABN: 51902674318
  </p>
</main>
</body>
</html>
```